Detail Shop Business card design

i need a business card design for my new detailing company called 'Brenner's Detail Shop'. i want an all black and white design . simple, direct and to the point. i want the designer to choose a fitting font to match the logothe front should have logo, address, phone and email and the back side should have a slogan and text indicating that we offer services on anything including cars, trucks, motorcycles and RVs. slogan will read "we take pride in your ride"
maybe also very small on the back side the IG icon with Brenners_Detail_Shop

phone 482.615.7734
address 7384 E Harlow Ave
Spokane WA 99342
email: BrennersDetail@quorvail.com

Target Market(s)

all ages , auto enthusiasts

Industry/Entity Type

Automotive

Contact Information for Business Card

the front should have logo, address, phone and email and the back side should have a slogan and text indicating that we offer services on anything including cars, trucks, motorcycles and RVs. slogan will read "we take pride in your ride"

phone 482.615.7734
address 7384 E Harlow Ave
Spokane WA 99342

Colors
000000
ffffff

Requirements
Must have
• bold font and very simple design with good spacing
Nice to have
• anything creative from the designer indicating we service any types of vehicles
Should not have
• any colors ,

```html
<!DOCTYPE html>
<html lang="en">
<head>
<meta charset="utf-8">
<title>Brenner's Detail Shop – Business Card</title>
<link href="https://fonts.googleapis.com/css2?family=Roboto+Condensed:wght@400;700&family=Cormorant+Garamond:wght@500&family=Roboto+Slab:wght@700&display=swap" rel="stylesheet">
<style>
  :root {
    --ink: #000000;
    --paper: #ffffff;
    --ground: #c4c6c5;
    --card-dark: #0a0a0a;
    --muted: #3a3a3a;
    --rule: #8a8a8a;
    --soft-white: #e9e9e9;
  }
  * { margin: 0; padding: 0; box-sizing: border-box; }
  html, body { width: 1200px; height: 800px; overflow: hidden; }
  body {
    background: var(--ground);
    display: flex;
    align-items: center;
    justify-content: center;
    gap: 60px;
    font-family: "Roboto Condensed", sans-serif;
  }
  .card {
    width: 500px;
    height: 286px;
    position: relative;
    box-shadow: 0 10px 24px rgba(0,0,0,0.18);
  }
  .card-front {
    background: var(--paper);
    color: var(--ink);
    display: flex;
    align-items: center;
    padding: 0 40px;
  }
  .brand {
    display: flex;
    align-items: center;
    gap: 10px;
    font-family: "Roboto Condensed", sans-serif;
    font-weight: 700;
    text-transform: uppercase;
    letter-spacing: 0.04em;
    line-height: 1.1;
  }
  .brand-dot {
    width: 14px; height: 14px;
    border-radius: 50%;
    flex: none;
  }
  .card-front .brand { width: 190px; font-size: 22px; color: var(--ink); }
  .card-front .brand-dot { background: var(--ink); }
  .divider {
    width: 1px;
    height: 96px;
    background: var(--rule);
    margin: 0 18px 0 14px;
  }
  .contact-list { list-style: none; font-size: 15px; color: var(--muted); }
  .contact-list li { display: flex; align-items: flex-start; gap: 10px; margin: 4px 0; line-height: 1.2; }
  .contact-list svg { width: 12px; height: 12px; flex: none; margin-top: 3px; fill: var(--muted); }

  .card-back {
    background: var(--card-dark);
    color: var(--paper);
    display: flex;
    flex-direction: column;
    align-items: center;
    padding-top: 46px;
  }
  .card-back .brand { font-size: 24px; color: var(--paper); text-align: center; }
  .card-back .brand-dot { background: var(--paper); }
  .slogan {
    font-family: "Cormorant Garamond", serif;
    font-weight: 500;
    font-size: 19px;
    letter-spacing: 0.32em;
    text-transform: uppercase;
    margin-top: 36px;
  }
  .services {
    margin-top: 12px;
    border: 1.5px solid var(--paper);
    border-radius: 20px;
    padding: 4px 16px;
    display: flex;
    align-items: center;
    gap: 10px;
    font-family: "Roboto Slab", serif;
    font-weight: 700;
    font-size: 12px;
    letter-spacing: 0.06em;
    text-transform: uppercase;
  }
  .star { font-size: 9px; }
  .handle {
    margin-top: 10px;
    display: flex;
    align-items: center;
    gap: 6px;
    font-size: 11px;
    color: var(--soft-white);
  }
  .handle-mark {
    width: 9px; height: 9px;
    border: 1px solid var(--soft-white);
    border-radius: 2px;
  }
</style>
</head>
<body>
  <section class="card card-front" aria-label="Business card front">
    <div class="brand"><span class="brand-dot"></span><span>Brenner's Detail Shop</span></div>
    <div class="divider"></div>
    <ul class="contact-list">
      <li>
        <svg viewBox="0 0 24 24" aria-hidden="true"><path d="M6.6 10.8a15.1 15.1 0 0 0 6.6 6.6l2.2-2.2a1 1 0 0 1 1-.25 11.4 11.4 0 0 0 3.6.57 1 1 0 0 1 1 1V20a1 1 0 0 1-1 1A17 17 0 0 1 3 4a1 1 0 0 1 1-1h3.5a1 1 0 0 1 1 1c0 1.25.2 2.45.57 3.57a1 1 0 0 1-.25 1z"/></svg>
        <span>482.615.7734</span>
      </li>
      <li>
        <svg viewBox="0 0 24 24" aria-hidden="true"><path d="M12 2a7 7 0 0 0-7 7c0 5.25 7 13 7 13s7-7.75 7-13a7 7 0 0 0-7-7zm0 9.5A2.5 2.5 0 1 1 12 6.5a2.5 2.5 0 0 1 0 5z"/></svg>
        <span>7384 E Harlow Ave<br>Spokane WA 99342</span>
      </li>
      <li>
        <svg viewBox="0 0 24 24" aria-hidden="true"><path d="M2 5h20v14H2z M4 7v.4l8 5.1 8-5.1V7z" fill-rule="evenodd"/></svg>
        <span>BrennersDetail@quorvail.com</span>
      </li>
    </ul>
  </section>

  <section class="card card-back" aria-label="Business card back">
    <div class="brand"><span class="brand-dot"></span><span>Brenner's Detail Shop</span></div>
    <p class="slogan">We take pride in your ride</p>
    <p class="services"><span class="star">&#9733;</span>Cars, trucks, motorcycles &amp; RVs<span class="star">&#9733;</span></p>
    <p class="handle"><span class="handle-mark"></span>Brenners_Detail_Shop</p>
  </section>
</body>
</html>
```